General Dental Office Business Card

I run a private general dental office in southern California, and would like a refresh/redesign of my business card. I focus on quality care rather than volume. The email address on the uploaded current card should be updated to: info@marbleshoredental.example. The current card's logo is a deboss, but I am open to other ideas. The logo can be refreshed, but it is something that's been with me since the beginning of the office, so I wouldn't want a drastic redesign.
Target Market(s)
Adults 18-99, whoever needs dental services
Industry/Entity Type
Healthcare/Dental
Contact Information for Business Card
Name, Address, Phone, email
Colors
Designer to choose colors to be used in the design.
Requirements
Must have
- Logo (Same as original one in the uploaded file), space on back for appointment time/date

```html
<!DOCTYPE html>
<html lang="en">
<head>
<meta charset="utf-8">
<title>Marble Shore Dental – Business Card</title>
<link href="https://fonts.googleapis.com/css2?family=Open+Sans:ital,wght@0,400;0,600;0,800;1,400;1,600&display=swap" rel="stylesheet">
<style>
  :root {
    --bg: #232323;
    --card: #ffffff;
    --sky: #8dd5ed;
    --sky-deep: #6ccbea;
    --sky-pale: #d3eef8;
    --ink: #555555;
    --rule: #666666;
  }
  * { box-sizing: border-box; margin: 0; padding: 0; }
  html, body { width: 1200px; height: 780px; overflow: hidden; background: var(--bg); }
  body { font-family: "Open Sans", Arial, sans-serif; position: relative; }

  .card {
    position: absolute; top: 75px; width: 360px; height: 630px;
    background: var(--card); border-radius: 26px; overflow: hidden;
  }
  .card--back { left: 190px; }
  .card--front { left: 650px; }

  /* Back: appointment side */
  .appt { position: absolute; left: 30px; right: 30px; top: 30px; }
  .appt__field { border-top: 1px solid var(--rule); text-align: center;
    font-style: italic; font-size: 12px; color: var(--ink); padding-top: 2px; margin-bottom: 28px; }
  .band { position: absolute; left: 0; right: 0; height: 54px; }
  .band--top { top: 118px; background: linear-gradient(to bottom, var(--sky-pale), var(--sky)); }
  .band--bottom { top: 470px; background: linear-gradient(to bottom, var(--sky), var(--sky-pale)); }
  .sea { position: absolute; left: 0; right: 0; top: 172px; height: 298px; background: var(--sky); }
  .mark { position: absolute; left: 50%; top: 40px; transform: translateX(-50%);
    width: 200px; height: 200px; border-radius: 50%;
    background: radial-gradient(circle at 35% 25%, #b9e4f4, var(--sky-deep));
    display: flex; align-items: center; justify-content: center; }
  .mark__name { color: #ffffff; font-weight: 600; font-size: 17px; text-align: center; line-height: 1.25; }
  .back__title { position: absolute; left: 0; right: 0; bottom: 30px; text-align: center;
    color: var(--sky); font-size: 34px; font-weight: 400; letter-spacing: 0.5px; }

  /* Front: contact side */
  .front__vertical { position: absolute; left: 4px; top: 18px; writing-mode: vertical-rl;
    color: var(--sky); font-weight: 800; font-size: 42px; line-height: 1; letter-spacing: 0.5px; }
  .logo { position: absolute; right: 36px; top: 28px; width: 164px; text-align: center; }
  .logo__disc { width: 164px; height: 142px; border-radius: 50%; background: var(--sky);
    display: flex; align-items: center; justify-content: center; }
  .logo__name { color: #ffffff; font-weight: 600; font-size: 15px; line-height: 1.25; }
  .contact { position: absolute; left: 56px; right: 8px; top: 382px; text-align: center; }
  .contact__name { color: var(--sky); font-weight: 800; font-size: 24px; line-height: 1.1; }
  .contact__role { color: var(--ink); font-weight: 600; font-size: 14px; margin-top: 2px; }
  .icons { display: flex; justify-content: center; gap: 8px; margin: 8px 0 8px; }
  .icon { width: 26px; height: 26px; border-radius: 50%; background: var(--sky);
    display: flex; align-items: center; justify-content: center; }
  .contact__line { color: var(--ink); font-size: 14px; font-weight: 600; line-height: 1.45; }
  .contact__pin { margin: 10px auto 4px; }
  .contact__address { color: var(--sky); font-size: 14px; font-weight: 600; font-style: italic; line-height: 1.4; }
</style>
</head>
<body>

<section class="card card--back" aria-label="Card back with appointment space">
  <div class="appt">
    <div class="appt__field">Appointment Date</div>
    <div class="appt__field">Time</div>
  </div>
  <div class="band band--top" role="img" aria-label="Decorative wave band"></div>
  <div class="sea">
    <div class="mark" role="img" aria-label="Practice emblem">
      <span class="mark__name">Marble Shore<br>Dental</span>
    </div>
  </div>
  <div class="band band--bottom" role="img" aria-label="Decorative wave band"></div>
  <h2 class="back__title">Marble Shore Dental</h2>
</section>

<section class="card card--front" aria-label="Card front with contact details">
  <h1 class="front__vertical">Marble Shore Dental</h1>
  <div class="logo">
    <div class="logo__disc">
      <span class="logo__name">Marble Shore<br>Dental</span>
    </div>
  </div>
  <div class="contact">
    <div class="contact__name">Daniel R. Moreno DDS</div>
    <div class="contact__role">General Dentistry</div>
    <div class="icons">
      <span class="icon" aria-label="Phone">
        <svg width="14" height="14" viewBox="0 0 24 24"><path d="M6.6 10.8a15 15 0 0 0 6.6 6.6l2.2-2.2c.3-.3.7-.4 1-.2 1.1.4 2.3.6 3.6.6.6 0 1 .4 1 1V20c0 .6-.4 1-1 1A17 17 0 0 1 3 4c0-.6.4-1 1-1h3.5c.6 0 1 .4 1 1 0 1.3.2 2.5.6 3.6.1.3 0 .7-.2 1z" fill="#fff"/></svg>
      </span>
      <span class="icon" aria-label="Email">
        <svg width="14" height="14" viewBox="0 0 24 24"><rect x="3" y="6" width="18" height="12" rx="1.5" fill="none" stroke="#fff" stroke-width="2"/><path d="M3 7l9 6 9-6" fill="none" stroke="#fff" stroke-width="2"/></svg>
      </span>
      <span class="icon" aria-label="Website">
        <svg width="14" height="14" viewBox="0 0 24 24"><circle cx="12" cy="12" r="9" fill="none" stroke="#fff" stroke-width="2"/><path d="M3 12h18M12 3c3 3 3 15 0 18M12 3c-3 3-3 15 0 18" fill="none" stroke="#fff" stroke-width="1.6"/></svg>
      </span>
    </div>
    <div class="contact__line">555-014-2828</div>
    <div class="contact__line">info@marbleshoredental.example</div>
    <div class="contact__line">www.marbleshoredental.example</div>
    <div class="icon contact__pin" aria-label="Address">
      <svg width="14" height="14" viewBox="0 0 24 24"><path d="M12 2a7 7 0 0 0-7 7c0 5 7 13 7 13s7-8 7-13a7 7 0 0 0-7-7z" fill="none" stroke="#fff" stroke-width="2"/><circle cx="12" cy="9" r="2.5" fill="#fff"/></svg>
    </div>
    <div class="contact__address">1200 Seabreeze Parkway<br>Coastview, CA 90000</div>
  </div>
</section>

</body>
</html>
```